MODELS AGENCY NEW YEAR 2026 CARD

A 10 cm x 21 cm horizontal New Year card for clients of our 2 models agencies, Brindel (kids) and Pavaduel (actors and adults) (logo in the jobs).

Side A of the card: creative mission:
-text: 2026
-text: Peace and Love
-Studio or movie set atmosphere
-tone of voice: optimistic, positive, colorful

Side B:
(name of 4 people of the agency:)
Solange, Anne-Sophie, Josiane & Paul-Henri,
(2 logos)
Brindel & PavaDuel
(Adres)
Rue des Tilleuls 74 b3 - 1060 Bruxelles - Belgique

Target Market(s)

Movie directors, photographers

Industry/Entity Type

Fashion, advertising & Movies

Requirements
Must have
• SEE TEXT IN BRIEFING

```html
<!DOCTYPE html>
<html lang="en">
<head>
<meta charset="utf-8">
<title>Brindel &amp; Pavaduel – New Year 2026 Card</title>
<link href="https://fonts.googleapis.com/css2?family=Bebas+Neue&family=Cinzel:wght@400;500&family=Montserrat:wght@400&display=swap" rel="stylesheet">
<style>
  :root {
    --page: #e4e4e4;
    --paper: #f6f5f1;
    --white: #ffffff;
    --ink: #1d1d22;
    --navy: #26307f;
    --gold: #d9a54a;
    --gold-soft: rgba(217,165,74,0.35);
    --amber: #e9ad35;
    --coral: #ef5b4f;
    --sage: #8cbf98;
    --tan: #c89a6e;
    --blue-bar: #009ad9;
  }
  * { margin: 0; padding: 0; box-sizing: border-box; }
  html, body { width: 1200px; height: 1200px; overflow: hidden; }
  body { background: var(--page); position: relative; font-family: "Montserrat", sans-serif; }

  .card {
    position: absolute; left: 235px; width: 730px; height: 348px;
    background: var(--paper); overflow: hidden;
  }
  .card--front { top: 225px; }
  .card--back  { top: 678px; }

  .garland {
    position: absolute; left: 0; top: 0; width: 100%; height: 90px;
    background:
      linear-gradient(to bottom, rgba(246,245,241,0) 55%, var(--paper) 100%),
      linear-gradient(to right, rgba(233,173,53,0.45), rgba(239,91,79,0.35), rgba(140,191,152,0.4), rgba(233,173,53,0.45), rgba(239,91,79,0.35), rgba(140,191,152,0.4), rgba(233,173,53,0.45));
  }
  .side-rule {
    position: absolute; top: 163px; height: 1px; width: 60px; background: var(--gold-soft);
  }
  .side-rule--left { left: 0; }
  .side-rule--right { right: 0; }

  .burst { position: absolute; border-radius: 50%; transform: translate(-50%, -50%); }
  .burst--navy { background: radial-gradient(circle, rgba(38,48,127,0.55) 0%, rgba(38,48,127,0.25) 55%, rgba(38,48,127,0) 72%); }
  .burst--gold { background: radial-gradient(circle, rgba(217,165,74,0.45) 0%, rgba(217,165,74,0.18) 55%, rgba(217,165,74,0) 72%); }
  .burst--dots { background: radial-gradient(circle, rgba(38,48,127,0.18) 0%, rgba(38,48,127,0.1) 60%, rgba(38,48,127,0) 72%); }
  .burst--spark { background: radial-gradient(circle, rgba(233,173,53,0.5) 0%, rgba(233,173,53,0) 70%); }

  .glasses {
    position: absolute; top: 270px; width: 70px; height: 78px;
    background: linear-gradient(to bottom, rgba(200,140,50,0.15), rgba(200,140,50,0.4));
    border-radius: 8px 8px 0 0;
  }

  /* Front */
  .emblem-ring {
    position: absolute; left: 240px; top: 51px; width: 250px; height: 250px;
    border: 1px solid var(--gold); border-radius: 50%; z-index: 2;
  }
  .emblem {
    position: absolute; left: 247px; top: 58px; width: 236px; height: 236px;
    background: var(--white); border: 1px solid var(--gold-soft); border-radius: 50%;
    z-index: 3; text-align: center;
  }
  .emblem__year {
    margin-top: 52px; font-family: "Bebas Neue", sans-serif; font-size: 40px; line-height: 1; letter-spacing: 1px;
  }
  .emblem__year span:nth-child(1) { color: var(--amber); }
  .emblem__year span:nth-child(2) { color: var(--tan); }
  .emblem__year span:nth-child(3) { color: var(--coral); }
  .emblem__year span:nth-child(4) { color: var(--sage); }
  .emblem__title {
    margin-top: 6px; font-family: "Cinzel", serif; font-size: 24px; line-height: 1; color: var(--ink); letter-spacing: 0.5px;
  }
  .emblem__title .big { font-size: 28px; }
  .emblem__tagline {
    margin-top: 8px; font-size: 13px; line-height: 18px; color: var(--ink); font-weight: 400;
  }
  .emblem__rule { width: 109px; height: 1px; background: var(--navy); margin: 7px auto 0; }
  .emblem__leaves {
    width: 74px; height: 38px; margin: 9px auto 0; border-radius: 0 0 37px 37px;
    background: linear-gradient(to bottom, rgba(38,48,127,0.1), rgba(38,48,127,0.3));
  }

  /* Back */
  .team-frame {
    position: absolute; left: 255px; top: 45px; width: 221px; height: 205px;
    border: 1px solid var(--gold); border-radius: 12px; z-index: 2;
  }
  .team {
    position: absolute; left: 260px; top: 50px; width: 211px; height: 195px;
    background: var(--white); border: 1px solid var(--gold-soft); border-radius: 9px; z-index: 3;
    display: flex; flex-direction: column; align-items: center; padding-top: 47px;
  }
  .team__name {
    font-family: "Cinzel", serif; font-size: 14px; color: var(--ink); letter-spacing: 0.6px; line-height: 18px;
  }
  .team__name .big { font-size: 16px; }
  .team__rule { width: 130px; height: 1px; background: var(--navy); margin: 9px 0 10px; }
  .team__rule:nth-of-type(1) { }
  .agencies {
    position: absolute; top: 269px; left: 0; width: 100%; display: flex; justify-content: center; gap: 22px;
  }
  .agency {
    font-family: "Montserrat", sans-serif; font-size: 11px; line-height: 18px; color: var(--navy); font-weight: 400;
    display: flex; align-items: center; gap: 5px;
  }
  .agency__dot { width: 7px; height: 7px; border-radius: 50%; background: var(--navy); }
  .address-bar {
    position: absolute; left: 0; top: 308px; width: 100%; height: 23px; background: var(--blue-bar);
    color: var(--white); font-size: 14.5px; line-height: 23px; text-align: center; letter-spacing: 0.2px;
  }
</style>
</head>
<body>

<section class="card card--front" aria-label="Card side A">
  <div class="garland" role="img" aria-label="Garland of hanging gold and green baubles with coral and orange stars"></div>
  <div class="side-rule side-rule--left"></div>
  <div class="side-rule side-rule--right"></div>

  <div class="burst burst--navy" role="img" aria-label="Navy firework burst" style="left:204px;top:129px;width:92px;height:92px"></div>
  <div class="burst burst--gold" role="img" aria-label="Gold firework burst" style="left:88px;top:163px;width:92px;height:92px"></div>
  <div class="burst burst--gold" role="img" aria-label="Gold firework burst" style="left:617px;top:163px;width:92px;height:92px"></div>
  <div class="burst burst--dots" role="img" aria-label="Dotted navy firework" style="left:517px;top:109px;width:70px;height:70px"></div>
  <div class="burst burst--navy" role="img" aria-label="Navy firework burst" style="left:493px;top:281px;width:92px;height:92px;z-index:4"></div>
  <div class="burst burst--dots" role="img" aria-label="Dotted navy firework" style="left:253px;top:294px;width:70px;height:70px"></div>
  <div class="burst burst--spark" role="img" aria-label="Small gold sparkle" style="left:210px;top:230px;width:36px;height:36px"></div>
  <div class="burst burst--spark" role="img" aria-label="Small gold sparkle" style="left:521px;top:189px;width:36px;height:36px"></div>
  <div class="burst burst--spark" role="img" aria-label="Small gold sparkle" style="left:55px;top:247px;width:40px;height:40px"></div>
  <div class="burst burst--spark" role="img" aria-label="Small gold sparkle" style="left:673px;top:244px;width:40px;height:40px"></div>

  <div class="glasses" role="img" aria-label="Two clinking champagne glasses" style="left:20px"></div>
  <div class="glasses" role="img" aria-label="Two clinking champagne glasses" style="left:644px"></div>

  <div class="emblem-ring"></div>
  <div class="emblem">
    <div class="emblem__year"><span>2</span><span>0</span><span>2</span><span>6</span></div>
    <h1 class="emblem__title"><span class="big">P</span>EACE &amp; <span class="big">L</span>OVE</h1>
    <p class="emblem__tagline">Studio or movie set<br>atmosphere.</p>
    <div class="emblem__rule"></div>
    <div class="emblem__leaves" role="img" aria-label="Navy leaf ornament"></div>
  </div>
</section>

<section class="card card--back" aria-label="Card side B">
  <div class="garland" role="img" aria-label="Garland of hanging gold and green baubles with coral and orange stars"></div>
  <div class="side-rule side-rule--left"></div>
  <div class="side-rule side-rule--right"></div>

  <div class="burst burst--navy" role="img" aria-label="Navy firework burst" style="left:206px;top:130px;width:62px;height:62px"></div>
  <div class="burst burst--gold" role="img" aria-label="Gold firework burst" style="left:117px;top:163px;width:92px;height:92px"></div>
  <div class="burst burst--gold" role="img" aria-label="Gold firework burst" style="left:617px;top:163px;width:92px;height:92px"></div>
  <div class="burst burst--navy" role="img" aria-label="Navy firework burst" style="left:517px;top:173px;width:62px;height:62px"></div>
  <div class="burst burst--dots" role="img" aria-label="Dotted navy firework" style="left:66px;top:261px;width:70px;height:70px"></div>
  <div class="burst burst--dots" role="img" aria-label="Dotted navy firework" style="left:669px;top:286px;width:70px;height:70px"></div>
  <div class="burst burst--spark" role="img" aria-label="Small gold sparkle" style="left:496px;top:247px;width:40px;height:40px"></div>
  <div class="burst burst--spark" role="img" aria-label="Small gold sparkle" style="left:224px;top:36px;width:40px;height:40px"></div>
  <div class="burst burst--spark" role="img" aria-label="Small gold sparkle" style="left:494px;top:24px;width:30px;height:30px"></div>

  <div class="team-frame"></div>
  <div class="team">
    <p class="team__name"><span class="big">S</span>OLANGE</p>
    <div class="team__rule"></div>
    <p class="team__name"><span class="big">A</span>NNE-<span class="big">S</span>OPHIE</p>
    <div class="team__rule"></div>
    <p class="team__name"><span class="big">J</span>OSIANE</p>
    <div class="team__rule"></div>
    <p class="team__name"><span class="big">P</span>AUL-<span class="big">H</span>ENRI</p>
  </div>

  <div class="agencies">
    <div class="agency"><span class="agency__dot"></span>Brindel</div>
    <div class="agency"><span class="agency__dot"></span>PavaDuel</div>
  </div>

  <div class="address-bar">Rue des Tilleuls 74 b3 - 1060 Bruxelles - Belgique</div>
</section>

</body>
</html>
```